Luxury Shimmer Oil for Face & Body

We need a label design for our gold shimmer oil. We are a luxury skincare company and this will be our highest priced item for sale. See uploaded pictures for our logo and what the bottle looks like. We will need a product label as well as a sample size version for our samples. We would like to see how the designs look on the bottle also (See uploaded pictures of the gold bottle we are using). https://www.velorabotanics.com/ is our website to use for reference.
We need our logo somewhere on the label.

Front of Label:

Shimmer
(Gold Face & Body Oil)
Vitamins C & E
Net Wt. 1.0 oz/30 mL

Back of Label:
Ingredients: Organic Jojoba Oil, Organic Grapeseed Oil, Ascorbic Acid (Vitamin C),
A Tocopheryl Acetate (Vitamin E), Gold Mica, Vanilla & Orange Essential Oils.

Directions: Shake bottle prior to use as natural separation may
occur. Apply generously to face, neck, and body. Can mix with
foundation for a beautiful glow and smoother application.

Warnings: External use only. Discontinue use if irritation occurs
or if you are allergic to any of the ingredients.

Manufactured & Distributed by: Velora Botanics LLC
P.O. Box 58603, Colorado Springs, CO. 80947
VeloraBotanics.com Made in U.S.A.

Label Dimension:

Height: 1.75 inches
Width: 3.5 inches

Sample Size Label:

Height: 1.25 inches
Width: 2 inches
We will only need the front portion of the label for the sample size with the Net Wt. 0.16oz/5mL

Target Market(s)

Women ages 40+

Industry/Entity Type

Skincare/beauty

Requirements
Must have
• Information on front and back of label, logo on the label.
Nice to have
• I would like a clear background of label. It needs to look elegant with pop but easy to read and tell what the product is. A flower or elegant design on the label would be nice, perhaps under, "Shimmer." Our logo could also go in this spot instead.
Should not have
• Golds which do not match the bottle. Best to stay away from gold as the gold bottles often differ in shade slightly.

```html
<!DOCTYPE html>
<html lang="en">
<head>
<meta charset="utf-8">
<title>Velora Botanics Shimmer Oil – Front Label</title>
<link rel="stylesheet" href="https://fonts.googleapis.com/css2?family=Cinzel:wght@600&family=Great+Vibes&family=Montserrat:wght@300;700&family=Arvo&display=swap">
<style>
  :root {
    --page: #ffffff;
    --ink: #000000;
    --label-center: #2e2e31;
    --label-edge: #070707;
    --gold: #d0a75b;
    --gold-light: #e6c98a;
    --gold-soft: rgba(201, 160, 92, 0.22);
    --cream: #f1ece2;
  }
  * { margin: 0; padding: 0; box-sizing: border-box; }
  html, body { width: 1200px; height: 800px; overflow: hidden; background: var(--page); }
  .canvas { position: relative; width: 1200px; height: 800px; }

  .label {
    position: absolute; left: 180px; top: 190px; width: 840px; height: 420px;
    overflow: hidden;
    background: radial-gradient(ellipse 55% 60% at 50% 52%, var(--label-center) 0%, #151516 55%, var(--label-edge) 100%);
  }
  .label > * { position: absolute; }

  .ornament {
    border-radius: 50%;
    background: radial-gradient(ellipse at center, var(--gold-soft) 0%, rgba(201,160,92,0.08) 55%, transparent 75%);
  }

  .rule-line { inset: 0; width: 840px; height: 420px; }

  .brand-mark {
    left: 230px; top: 78px; width: 76px; height: 76px;
    border-radius: 50%; background: var(--gold);
  }
  .brand-name, .brand-sub {
    font-family: "Cinzel", serif; font-weight: 600; color: var(--gold);
    white-space: nowrap;
  }
  .brand-name { left: 328px; top: 72px; font-size: 56px; line-height: 1; letter-spacing: 1px; }
  .brand-sub { left: 334px; top: 130px; font-size: 25px; line-height: 1; letter-spacing: 12px; }

  .product-script {
    left: 270px; top: 180px; font-family: "Great Vibes", cursive;
    font-size: 108px; line-height: 1; color: var(--gold);
  }
  .product-type {
    left: 536px; top: 192px; font-family: "Montserrat", sans-serif; font-weight: 700;
    font-size: 90px; line-height: 1; color: var(--gold); letter-spacing: -2px;
  }
  .product-desc {
    left: 322px; top: 274px; font-family: "Arvo", serif; font-size: 27px;
    line-height: 1; color: var(--gold-light); white-space: nowrap;
  }

  .facts { left: 496px; top: 332px; list-style: none; }
  .facts li {
    font-family: "Montserrat", sans-serif; font-weight: 300; font-size: 16px;
    line-height: 20px; color: var(--cream); padding-left: 20px; position: relative;
  }
  .facts li::before {
    content: ""; position: absolute; left: 0; top: 6px; width: 8px; height: 8px;
    border: 2px solid var(--gold); border-radius: 50%;
  }

  .caption {
    position: absolute; left: 0; width: 1200px; top: 640px; text-align: center;
    font-family: "Montserrat", sans-serif; font-weight: 300; font-size: 42px; color: var(--ink);
  }
</style>
</head>
<body>
<main class="canvas">
  <section class="label">
    <div class="ornament" style="left:0;top:14px;width:84px;height:68px" role="img" aria-label="Gold line-art leafy branch"></div>
    <div class="ornament" style="left:324px;top:0;width:160px;height:54px" role="img" aria-label="Gold line-art flowers and leaves"></div>
    <div class="ornament" style="left:692px;top:0;width:80px;height:50px" role="img" aria-label="Gold line-art blossom"></div>
    <div class="ornament" style="left:636px;top:128px;width:90px;height:62px" role="img" aria-label="Gold line-art five-petal flower"></div>
    <div class="ornament" style="left:788px;top:130px;width:52px;height:124px" role="img" aria-label="Gold line-art flowering stem"></div>
    <div class="ornament" style="left:32px;top:202px;width:76px;height:60px" role="img" aria-label="Gold line-art five-petal flower"></div>
    <div class="ornament" style="left:242px;top:250px;width:38px;height:40px" role="img" aria-label="Gold line-art sprig"></div>
    <div class="ornament" style="left:0;top:314px;width:40px;height:96px" role="img" aria-label="Gold line-art leafy stem"></div>
    <div class="ornament" style="left:128px;top:354px;width:76px;height:66px" role="img" aria-label="Gold line-art flowering branch"></div>
    <div class="ornament" style="left:232px;top:318px;width:64px;height:60px" role="img" aria-label="Gold line-art open flower"></div>
    <div class="ornament" style="left:388px;top:346px;width:76px;height:74px" role="img" aria-label="Gold line-art flowering branch"></div>
    <div class="ornament" style="left:752px;top:302px;width:88px;height:84px" role="img" aria-label="Gold line-art leafy branch"></div>

    <svg class="rule-line" viewBox="0 0 840 420" aria-hidden="true">
      <g stroke="#c9a45c" stroke-width="1.2" fill="#c9a45c">
        <line x1="248" y1="62" x2="558" y2="62"/>
        <circle cx="248" cy="62" r="3.5"/><circle cx="558" cy="62" r="3.5"/>
        <line x1="316" y1="162" x2="624" y2="162"/>
        <circle cx="316" cy="162" r="3.5"/><circle cx="624" cy="162" r="3.5"/>
      </g>
      <g fill="#c9a45c">
        <circle cx="132" cy="11" r="3.5"/><circle cx="551" cy="28" r="3.5"/>
        <circle cx="806" cy="64" r="2"/><circle cx="107" cy="336" r="3.5"/>
        <circle cx="243" cy="305" r="2"/><circle cx="726" cy="252" r="1.5"/>
        <circle cx="778" cy="238" r="1.5"/><circle cx="700" cy="336" r="1.5"/>
        <circle cx="108" cy="216" r="3"/>
      </g>
    </svg>

    <div class="brand-mark" aria-hidden="true"></div>
    <div class="brand-name">VELORA</div>
    <div class="brand-sub">BOTANICS</div>

    <div class="product-script">Shimmer</div>
    <div class="product-type">OIL</div>
    <div class="product-desc">GOLD FACE &amp; BODY OIL</div>

    <ul class="facts">
      <li>VITAMINS C &amp; E</li>
      <li>NET WT. 1.0 OZ/30 ML</li>
    </ul>
  </section>

  <p class="caption">Front Design</p>
</main>
</body>
</html>
```